Banner Ad Design Project

I need to design a banner that is going to be placed out the front of rural pubs in central Queensland. My company provides female adult entertainment (topless/lingerie/bikini waitresses, girls doing shows/entertaining, disco setting, mechanical bull & surf board, sumo wrestling, jousting, bouncy boxing, twister, jelly & lube wrestling) to pubs in mining towns throughout central Queensland. These games on offer are interactive with patrons, as they can participate. At this stage my company will be offering this type of entertainment once month and each month at each venue, the entertainment type will change every month eg. month 1 mechanical bull, month 2 bouncy boxing, month 3 sumo wrestling, month 4 mechanical surf board. In saying this I need the banner to be quiet generic and therefore not relate to one specific type of entertainment for example boxing. I will be putting flyers that are specific to the entertainment in the bottle shops & pub every month, therefore providing them with more detail on the events. Therefore I need this banner to be eye catching, sexy and appealing to a large group of men that are in the mining industry (coal). These guys are stuck in rural/remote locations for extended periods of time and crave female interaction, atmosphere, entertainment, arse, boobs and sex. The girls my company provides are top quality and often feature in Brisk/Velvetine/Kip/Lanternhall Magazine, Miss Glimmer Australia etc. Therefore the banner needs to replicate beauty.
Updates

Just a thought, the text must stand out and be visable to people driving past pub on the road side. Therefore must be bold, striking and modern.

Preferable a blonde girl because she will capture the audience more. 

Target Market(s)

Male coal miners in the Bowen Basin - Central Queensland. Work force is predominantly fly in fly out

Industry/Entity Type

Entertainment

Requirements
Must have
• - new gorgious girls every month
- new interactive games/entertainment every month
- enquire within dates/times
- my logo
- my company fb

I am open to suggestion with what i need.
Nice to have
• - sexy gril either in lingerie/bikini with big boobs
- could try a mining theme?

```html
<!DOCTYPE html>
<html lang="en">
<head>
<meta charset="utf-8">
<title>MarisolVane – Banner</title>
<link rel="stylesheet" href="https://fonts.googleapis.com/css2?family=Arimo:wght@400;700&display=swap">
<style>
  :root {
    --bg-light: #f6c9b6;
    --bg-mid: #ef9f8e;
    --bg-deep: #e27a72;
    --silhouette: #d9776c;
    --brand-box: #1a1114;
    --brand-text: #ffffff;
    --accent-band: #e4157c;
    --photo-light: #c98a6a;
    --photo-dark: #6b3a2c;
    --headline: #111111;
    --headline-glow: rgba(255, 236, 228, 0.85);
    --service-text: #f4f000;
    --service-shadow: #3a1a12;
  }
  * { margin: 0; padding: 0; box-sizing: border-box; }
  html, body { width: 1200px; height: 480px; overflow: hidden; background: #ffffff; }
  .banner {
    position: relative;
    width: 1200px;
    height: 480px;
    overflow: hidden;
    background: radial-gradient(ellipse at 45% 40%, var(--bg-light) 0%, var(--bg-mid) 55%, var(--bg-deep) 100%);
    font-family: "Arimo", Arial, sans-serif;
  }
  .banner__art { position: absolute; inset: 0; width: 1200px; height: 480px; }
  .brand {
    position: absolute;
    left: 0; top: 0;
    width: 194px; height: 48px;
    background: var(--brand-box);
    display: flex; align-items: center;
    padding-left: 8px;
  }
  .brand__name {
    color: var(--brand-text);
    font-weight: 400;
    font-size: 25px;
    letter-spacing: -0.5px;
  }
  .headlines {
    position: absolute;
    left: 22px; top: 106px;
    list-style: none;
  }
  .headlines__item {
    color: var(--headline);
    font-weight: 700;
    font-size: 27px;
    line-height: 60px;
    letter-spacing: -0.3px;
    text-shadow: 0 0 4px var(--headline-glow), 0 0 8px var(--headline-glow);
  }
  .services {
    position: absolute;
    left: 86px; top: 342px;
    width: 1080px;
    color: var(--service-text);
    font-weight: 400;
    font-size: 26px;
    line-height: 39px;
    text-shadow: 1px 1px 0 var(--service-shadow), 0 0 3px var(--service-shadow);
  }
</style>
</head>
<body>
  <div class="banner">
    <svg class="banner__art" viewBox="0 0 1200 480" xmlns="http://www.w3.org/2000/svg">
      <defs>
        <linearGradient id="photoTone" x1="0" y1="0" x2="1" y2="1">
          <stop offset="0" stop-color="var(--photo-light)"/>
          <stop offset="0.6" stop-color="#a0604a"/>
          <stop offset="1" stop-color="var(--photo-dark)"/>
        </linearGradient>
        <linearGradient id="silhouetteTone" x1="0" y1="0" x2="1" y2="0">
          <stop offset="0" stop-color="var(--silhouette)" stop-opacity="0.85"/>
          <stop offset="1" stop-color="var(--silhouette)" stop-opacity="0.35"/>
        </linearGradient>
      </defs>
      <path class="silhouette" role="img" aria-label="Faint side silhouette of a woman's head and hair"
            d="M0 50 C90 50 150 120 150 230 C150 330 110 400 80 480 L0 480 Z"
            fill="url(#silhouetteTone)"/>
      <path class="feature-photo" role="img" aria-label="Photo of a model in a red bikini reclining on a wicker chair"
            d="M610 480 Q820 150 1200 14 L1200 480 Z"
            fill="url(#photoTone)"/>
      <path class="accent-band" d="M596 480 Q810 140 1200 2" fill="none" stroke="var(--accent-band)" stroke-width="16"/>
      <path class="accent-line" d="M612 480 Q822 154 1200 17" fill="none" stroke="#ffffff" stroke-width="2" stroke-opacity="0.7"/>
    </svg>

    <div class="brand">
      <span class="brand__name">MarisolVane</span>
    </div>

    <ul class="headlines">
      <li class="headlines__item">New Interactive Games/Entertainment Every Month</li>
      <li class="headlines__item">New Gorgious Girls Every Month</li>
      <li class="headlines__item">We Provides Female Adult Entertainment.</li>
    </ul>

    <p class="services">(topless/lingerie/bikini waitresses, girls doing shows/entertaining, disco setting, mechanical bull &amp; surf board, sumo wrestling, jousting, bouncy boxing, twister, jelly &amp; lube wrestling)</p>
  </div>
</body>
</html>
```